Business Card - Existing Logo & Branding copied to Business Card Format

We are looking for a designer to help with designing a two sided business card for us. We sell a web based software platform that helps people sell access to online training.
We have an existing logo and recently completed a design project here on draft hive to have someone design a nice trade show booth for us (also attached file for that design as well as our logo). We really like the look and feel of the tradeshow booth design. The fonts, colors, etc all work for us. We are hoping someone can create something very similar just in business card format.
Should be pretty straight forward hopefully....
On one side we want the logo, employee name, email address, phone and fax. On the other side we would like the text "transform your organizations training, revenue products = revenue" - See the attached PSD for what we want that to look like.
You can also see our website at www.tutorvane.com for an example of our branding.
We are open to ideas, have done several projects on draft hive and love when designers come up with creative approaches that are even better then what we envisioned.
Software

```html
<!DOCTYPE html>
<html lang="en">
<head>
<meta charset="utf-8">
<title>TutorVane Business Card Options</title>
<link rel="stylesheet" href="https://fonts.googleapis.com/css2?family=Exo+2:wght@400;600;700&display=swap">
<style>
  :root {
    --brand-red: #b01f2a;
    --brand-red-dark: #9a1a24;
    --ink: #3a3a3c;
    --band-grey: #3d3f44;
    --paper: #ffffff;
    --stage: #f1efeb;
    --label: #222222;
  }
  * { margin: 0; padding: 0; box-sizing: border-box; }
  html, body {
    width: 1200px; height: 1172px; overflow: hidden;
    background: var(--stage);
    font-family: "Exo 2", Arial, sans-serif;
  }
  .canvas { position: relative; width: 1200px; height: 1172px; }
  .option-label {
    position: absolute; left: 0; width: 1200px; text-align: center;
    font-size: 22px; font-weight: 400; color: var(--label);
  }
  .card {
    position: absolute; width: 552px; height: 316px; overflow: hidden;
    box-shadow: 0 3px 10px rgba(0,0,0,0.18);
  }
  .card--front { left: 40px; background: var(--paper); }
  .card--back { left: 620px; background: var(--brand-red); color: #fff; }
  .row-one { top: 183px; }
  .row-two { top: 785px; }

  .wordmark {
    position: absolute; display: flex; align-items: center;
    font-weight: 700; letter-spacing: -0.5px; color: var(--ink);
  }
  .wordmark__square { display: inline-block; background: var(--brand-red); margin-right: 12px; }
  .wordmark--small { left: 20px; top: 46px; font-size: 40px; }
  .wordmark--small .wordmark__square { width: 40px; height: 40px; }
  .wordmark--large { left: 0; width: 552px; justify-content: center; top: 90px; font-size: 56px; }
  .wordmark--large .wordmark__square { width: 54px; height: 54px; }
  .wordmark--reverse { left: 22px; top: 48px; font-size: 40px; color: #fff; }
  .wordmark--reverse .wordmark__square { width: 40px; height: 40px; background: #fff; }

  .person { position: absolute; color: var(--brand-red); }
  .person__name { font-size: 20px; font-weight: 700; line-height: 1; }
  .person__title { font-size: 9px; font-weight: 600; letter-spacing: 4px; color: var(--ink); margin-top: 4px; }
  .person--side { left: 392px; top: 56px; padding-left: 12px; border-left: 2px solid var(--brand-red); }
  .person--centered { left: 0; width: 552px; text-align: center; top: 198px; }
  .person--centered .person__name { display: inline-block; padding-bottom: 4px; border-bottom: 1px solid #d8d8d8; }

  .base-bands { position: absolute; left: 0; bottom: 0; width: 552px; height: 24px; }

  .contact-list { position: absolute; left: 18px; list-style: none; }
  .contact-list li {
    display: flex; align-items: center; height: 26px;
    font-size: 19px; font-weight: 600; white-space: nowrap;
  }
  .contact-list svg { width: 16px; height: 16px; margin-right: 12px; flex: none; }
  .row-one .contact-list { top: 172px; }
  .row-two .contact-list { top: 222px; }
</style>
</head>
<body>
<main class="canvas">

  <p class="option-label" style="top:86px;">Option_01</p>

  <section class="card card--front row-one">
    <div class="wordmark wordmark--small"><span class="wordmark__square"></span>TutorVane</div>
    <div class="person person--side">
      <p class="person__name">Noor Haldane</p>
      <p class="person__title">DIRECTOR</p>
    </div>
    <svg class="base-bands" viewBox="0 0 552 24" preserveAspectRatio="none">
      <polygon points="0,4 262,4 282,24 0,24" fill="var(--band-grey)"/>
      <polygon points="270,4 276,4 296,24 290,24" fill="#fff"/>
      <polygon points="280,12 552,12 552,24 292,24" fill="var(--brand-red)"/>
    </svg>
  </section>

  <section class="card card--back row-one">
    <ul class="contact-list">
      <li><svg viewBox="0 0 16 16"><path d="M8 1a5 5 0 0 0-5 5c0 4 5 9 5 9s5-5 5-9a5 5 0 0 0-5-5zm0 7a2 2 0 1 1 0-4 2 2 0 0 1 0 4z" fill="#fff"/></svg>xxxxxxx-xxx</li>
      <li><svg viewBox="0 0 16 16"><rect x="1" y="3" width="14" height="10" rx="1" fill="#fff"/><path d="M1.5 3.5L8 9l6.5-5.5" stroke="var(--brand-red)" stroke-width="1.4" fill="none"/></svg>info@tutorvane.com</li>
      <li><svg viewBox="0 0 16 16"><path d="M4 1l2.5 3-1.5 2c1 2 3 4 5 5l2-1.5 3 2.5-1.5 2.5C8 15 1 8 1.5 2.5z" fill="#fff"/></svg>+800-555-0142</li>
      <li><svg viewBox="0 0 16 16"><rect x="4" y="1" width="8" height="5" fill="#fff"/><rect x="1" y="7" width="14" height="7" rx="1" fill="#fff"/><rect x="4" y="10" width="8" height="2" fill="var(--brand-red)"/></svg>+00000000</li>
      <li><svg viewBox="0 0 16 16"><circle cx="8" cy="8" r="6.5" fill="none" stroke="#fff" stroke-width="1.5"/><path d="M1.5 8h13M8 1.5c-3 3.5-3 9.5 0 13M8 1.5c3 3.5 3 9.5 0 13" stroke="#fff" stroke-width="1.2" fill="none"/></svg>www.tutorvane.com</li>
    </ul>
  </section>

  <p class="option-label" style="top:694px;">Option_02</p>

  <section class="card card--front row-two">
    <div class="wordmark wordmark--large"><span class="wordmark__square"></span>TutorVane</div>
    <div class="person person--centered">
      <p class="person__name">Noor Haldane</p>
      <p class="person__title">DIRECTOR</p>
    </div>
    <svg class="base-bands" viewBox="0 0 552 24" preserveAspectRatio="none">
      <polygon points="0,4 262,4 282,24 0,24" fill="var(--band-grey)"/>
      <polygon points="270,4 276,4 296,24 290,24" fill="#fff"/>
      <polygon points="280,12 552,12 552,24 292,24" fill="var(--brand-red)"/>
    </svg>
  </section>

  <section class="card card--back row-two">
    <div class="wordmark wordmark--reverse"><span class="wordmark__square"></span>TutorVane</div>
    <ul class="contact-list">
      <li><svg viewBox="0 0 16 16"><path d="M8 1a5 5 0 0 0-5 5c0 4 5 9 5 9s5-5 5-9a5 5 0 0 0-5-5zm0 7a2 2 0 1 1 0-4 2 2 0 0 1 0 4z" fill="#fff"/></svg>xxxxxxx-xxx</li>
      <li><svg viewBox="0 0 16 16"><rect x="1" y="3" width="14" height="10" rx="1" fill="#fff"/><path d="M1.5 3.5L8 9l6.5-5.5" stroke="var(--brand-red)" stroke-width="1.4" fill="none"/></svg>info@tutorvane.com</li>
      <li><svg viewBox="0 0 16 16"><path d="M4 1l2.5 3-1.5 2c1 2 3 4 5 5l2-1.5 3 2.5-1.5 2.5C8 15 1 8 1.5 2.5z" fill="#fff"/></svg>+800-555-0142</li>
    </ul>
  </section>

</main>
</body>
</html>
```